Private Investment Firm Needs PowerPoint Presentation Template

Design PowerPoint template, take Ridgefell-submitted rough presentation draft, and drop it into new template. See attached Project Brief file for more detail.
Updates

Some decent designs have been submitted but they seem to lack the understanding of our target markets. I am hopeful that more time and feedback will result in better results.

Target Market(s)

Private company owners and intermediaries.

Font styles to use
Serif

Colors
3176b5

Requirements
Must have
• See attached Project Brief.
Nice to have
Should not have
• No B2C fluff--this is a B2B project.

```html
<!DOCTYPE html>
<html lang="en">
<head>
<meta charset="utf-8">
<title>Ridgefell Capital – Non-Control Capital Deck</title>
<link href="https://fonts.googleapis.com/css2?family=Cinzel:wght@400;600;700&family=Open+Sans:wght@400;600;700&family=Montserrat:wght@400;500&display=swap" rel="stylesheet">
<style>
:root{
  --blue:#3176b5;
  --blue-deep:#0a63b5;
  --blue-navy:#0b4a8a;
  --blue-ink:#0e1a33;
  --sky:#4cc0e8;
  --charcoal:#55585c;
  --ink:#333;
  --muted:#666;
  --board:#a7a7a7;
}
*{box-sizing:border-box;margin:0;padding:0}
html,body{width:1043px;height:1200px;overflow:hidden}
body{background:radial-gradient(ellipse at center,#c4c4c4 0%,var(--board) 80%);font-family:"Open Sans",Arial,sans-serif;color:var(--ink);position:relative}
.slide{position:absolute;width:442px;height:250px;background:linear-gradient(160deg,#fff 0%,#f3f3f3 55%,#e6e6e6 100%);overflow:hidden;box-shadow:0 3px 8px rgba(0,0,0,.35)}
.slide::before{content:"";position:absolute;inset:0;background:var(--charcoal);clip-path:polygon(0 0,42px 0,0 140px)}
.slide::after{content:"";position:absolute;inset:0;background:linear-gradient(180deg,var(--blue-deep),#1e86d0 60%,#3a9ee0);clip-path:polygon(425px 0,442px 0,442px 250px,352px 250px)}
.slide>*{position:absolute;z-index:1}
.c1{left:50px}.c2{left:545px}
.r1{top:50px}.r2{top:340px}.r3{top:615px}.r4{top:900px}

.brand{display:flex;align-items:center;gap:4px;font-family:"Cinzel",serif;font-weight:600;color:var(--blue-navy);font-size:8px;letter-spacing:.5px}
.brand i{width:11px;height:11px;border-radius:50%;background:var(--blue-navy);display:block}
.foot-brand{left:46px;top:222px}
.url{top:225px;left:0;width:442px;text-align:center;font-size:7px;color:#222}
.url b{color:var(--blue-navy);font-weight:600}
.pg{left:412px;top:226px;font-size:6px;color:#fff;font-weight:700}

/* cover */
.cover-title{top:48px;left:0;width:442px;text-align:center;font-family:"Cinzel",serif;font-size:20px;line-height:23px;color:var(--blue-deep)}
.cover-sub{top:116px;left:0;width:442px;text-align:center;font-size:6.5px;line-height:9px;color:var(--muted)}
.cover-sub b{color:var(--blue-deep);font-weight:600}
.cover-date{top:143px;left:171px;width:100px;height:26px;border:1px solid #777;display:flex;align-items:center;justify-content:center;font-size:14px;color:#444;background:#fff}
.cover-brand{top:192px;left:180px;font-size:10px}
.cover-brand i{width:16px;height:16px}
.cover-url{top:228px;left:0;width:442px;text-align:center;font-size:9.5px;color:#222}
.cover-url b{color:var(--blue-navy);font-weight:600}

/* intro */
.h-intro{top:30px;left:0;width:410px;text-align:center;font-size:13.5px;font-weight:700;color:var(--blue-deep);letter-spacing:.5px}
.bullets{top:63px;left:52px;width:320px;list-style:none;font-size:6.3px;line-height:8px;color:#444}
.bullets>li{position:relative;padding-left:14px;margin-bottom:7px}
.bullets>li::before{content:"•";position:absolute;left:2px;color:var(--blue)}
.ticks{list-style:none;margin-top:1px}
.ticks li{padding-left:16px;position:relative}
.ticks li::before{content:"✓";position:absolute;left:4px;color:var(--blue);font-size:6px}

/* banner */
.banner{height:34px;background:var(--blue-deep);color:#fff;font-family:"Cinzel",serif;text-align:center;display:flex;align-items:center;justify-content:center;clip-path:polygon(10px 0,100% 0,calc(100% - 10px) 100%,0 100%)}
.banner-edge{width:6px;background:var(--charcoal);transform:skewX(-17deg)}

/* questionnaire */
.q-head{top:14px;left:0;width:442px;text-align:center;font-size:9px;font-weight:600;color:#333}
.q-banner{top:33px;left:66px;width:330px;font-size:9.5px;line-height:11px}
.q-tab{top:72px;left:180px;width:82px;height:13px;background:#111;color:#fff;font-size:7.5px;font-weight:700;text-align:center;line-height:13px;clip-path:polygon(5px 0,100% 0,calc(100% - 5px) 100%,0 100%)}
.q-col{top:92px;width:172px;font-size:4.3px;line-height:5.2px;color:#444}
.q-col.left{left:34px}.q-col.right{left:232px;width:160px}
.q{position:relative;padding-left:12px;margin-bottom:5px}
.q .n{position:absolute;left:0;top:0;width:8px;height:8px;border-radius:50%;background:var(--blue);color:#fff;font-size:5px;line-height:8px;text-align:center;font-weight:700}
.q strong{color:#222;font-weight:700;display:block}
.q em{font-style:normal;color:var(--blue);font-weight:700}

/* capital stack */
.s-edge1{top:24px;left:40px;height:28px}
.s-banner{top:24px;left:50px;width:326px;height:28px;font-size:11px}
.s-edge2{top:24px;left:380px;height:28px}
.stack-bar{top:57px;left:54px;width:346px;height:16px;background:var(--sky);font-size:6.5px;font-weight:700;text-align:center;line-height:16px;color:#111}
.tier{left:54px;width:116px;font-size:4.5px;color:#333}
.tier .lbl{background:var(--blue-deep);color:#fff;font-size:6.5px;font-weight:700;text-align:center;height:11px;line-height:11px;margin-bottom:1px}
.tier .row{background:linear-gradient(#fafafa,#ddd);height:11px;line-height:11px;text-align:center;margin-bottom:1px}
.tier.senior{top:77px}.tier.junior{top:170px}
.sbox{left:174px;width:226px;color:#fff;font-size:4.4px;line-height:5.4px;text-align:center;display:flex;flex-direction:column;justify-content:center;padding:0 10px}
.sbox b{font-size:5px;display:block;margin-bottom:1px}
.sbox.senior{top:77px;height:72px;background:var(--blue-navy)}
.sbox.junior{top:170px;height:56px;background:var(--blue-ink)}
.dash{top:158px;left:54px;width:346px;height:3px;background:repeating-linear-gradient(90deg,var(--blue-deep) 0 52px,var(--sky) 52px 72px)}

/* epilogue */
.epi{top:105px;left:0;width:442px;text-align:center;font-family:"Montserrat",sans-serif;font-size:29px;letter-spacing:1px;color:#444}
.epi-rule{top:148px;left:209px;width:24px;height:3px;background:var(--blue-deep)}

/* quote */
.qmark{font-family:Georgia,serif;font-size:52px;color:#c5c5c5;line-height:1}
.qm-open{top:20px;left:92px}
.qm-close{top:160px;left:278px}
.quote{top:68px;left:94px;width:240px;font-family:"Montserrat",sans-serif;font-size:10.3px;line-height:11.5px;color:#333}
.cite{top:170px;left:145px;font-size:6.5px;font-weight:700;color:var(--blue-deep)}

/* uses grid */
.u-title{top:28px;left:0;width:410px;text-align:center;font-size:14px;font-weight:700;color:var(--blue-deep)}
.uses{top:50px;left:54px;width:332px;display:grid;grid-template-columns:repeat(4,1fr);grid-template-rows:repeat(3,50px);gap:2px}
.use{background:linear-gradient(#f7f7f7,#dedede);text-align:center;padding:3px 4px 0;font-size:3.6px;line-height:4.3px;color:#555}
.use b{display:block;font-size:6px;line-height:6.6px;color:var(--blue-deep);margin-bottom:2px}

/* contact */
.ct-banner{top:18px;left:158px;width:140px;height:20px;font-family:"Montserrat",sans-serif;font-size:15px;letter-spacing:.5px;clip-path:polygon(7px 0,100% 0,calc(100% - 7px) 100%,0 100%)}
.ct-edge1{top:18px;left:151px;height:20px;width:5px}
.ct-edge2{top:18px;left:300px;height:20px;width:5px}
.ct-line{top:52px;left:52px;width:1px;height:125px;background:#aaa}
.ct{left:66px;font-size:7px;line-height:8.6px;color:#444}
.ct::before{content:"";position:absolute;left:-17px;top:1px;width:6px;height:6px;border-radius:50%;background:#fff;border:2px solid var(--blue-navy)}
.ct strong{color:var(--blue-deep);font-weight:700}
.ct .bl{color:var(--blue-deep)}
.ct1{top:52px}.ct2{top:118px}.ct3{top:167px}
.portrait{top:97px;left:318px;width:94px;height:94px;border-radius:50%;border:3px solid #fff;background:radial-gradient(circle at 50% 40%,#9fb6cc,#3d6e9e 70%,#234a72);box-shadow:0 1px 4px rgba(0,0,0,.3)}
</style>
</head>
<body>

<!-- 1 Cover -->
<section class="slide c1 r1">
  <h1 class="cover-title">Introduction to<br>Non-Control Capital</h1>
  <p class="cover-sub">The Lower Middle Market Private Company Strategy for<br>Raising Capital While <b>Maintaining Business Control</b></p>
  <div class="cover-date">Fall-2018</div>
  <div class="brand cover-brand"><i></i>Ridgefell</div>
  <p class="cover-url">www.<b>ridgefellcapital</b>.com</p>
</section>

<!-- 2 Introduction -->
<section class="slide c2 r1">
  <h2 class="h-intro">INTRODUCTION</h2>
  <ul class="bullets">
    <li>Private company owners have traditionally considered two capital raising options
      <ul class="ticks"><li>Borrow from a local bank, or</li><li>Sell most or all of the company to a change-of-control investor (aka Buyout firm)</li></ul></li>
    <li>An alternative most have not considered is the raising of Non-Control Capital, or capital that is invested into the business yet allows those same owners to retain controlling interest in their company</li>
    <li>Non-Control Capital is not appropriate for every private company owner but neither is a Change-of-Control sale</li>
    <li>The key is to determine what the business and owners require, and then partner with an investor best aligned with those needs so that long-term company growth, and personal goals, can both be achieved</li>
  </ul>
  <div class="brand foot-brand"><i></i>Ridgefell</div>
  <p class="url">www.<b>ridgefellcapital</b>.com</p>
  <span class="pg">1.</span>
</section>

<!-- 3 Questionnaire -->
<section class="slide c1 r2">
  <p class="q-head">Non-Control Capital Questionnaire</p>
  <div class="banner q-banner">The Critical Questions to Ask of<br>Any Prospective Non-Control Investor</div>
  <div class="q-tab">Questions</div>
  <div class="q-col left">
    <div class="q"><span class="n">1</span><strong>How many years has the firm been investing Non-Control Capital?</strong><em>Best Answer:</em> 5+ years investing as a team within the current firm. Indicates comfort and experience evaluating and making investments with each other.</div>
    <div class="q"><span class="n">2</span><strong>How many fully-invested Non-Control Capital funds in the firm's history?</strong><em>Best Answer:</em> 2+ fully-invested funds. Indicates experience and ability to close deals with the current regime.</div>
    <div class="q"><span class="n">3</span><strong>What percentage of the firm's voting investment committee are full-time Non-Control investors?</strong><em>Best Answer:</em> Super-majority. Indicates commitment, experience and focus on NCC.</div>
    <div class="q"><span class="n">4</span><strong>What is the number of Non-Control Capital investments made with the current firm and team?</strong><em>Best Answer:</em> 20+. Indicates long-term experience and comfort with current team.</div>
  </div>
  <div class="q-col right">
    <div class="q"><span class="n">5</span><strong>What percentage of portfolio investments made are "sponsorless" (those without a change-of-control investor)?</strong><em>Best Answer:</em> 80%+ of all investments closed in the last 5 years. Indicates ability to add value as a sole investor, not a backup.</div>
    <div class="q"><span class="n">6</span><strong>Can the investor show quantifiable proof of their ability to assist portfolio companies with growth and improvement?</strong><em>Best Answer:</em> Yes. Owners should evaluate investors on actual historical revenue, EBITDA and employee growth. Indicates true value-added ability to help owners grow their businesses over time.</div>
  </div>
  <div class="brand foot-brand"><i></i>Ridgefell</div>
  <p class="url">www.<b>ridgefellcapital</b>.com</p>
  <span class="pg">2.</span>
</section>

<!-- 4 Capital stack -->
<section class="slide c2 r2">
  <div class="banner-edge s-edge1"></div>
  <div class="banner s-banner">Ridgefell Provides Junior Capital</div>
  <div class="banner-edge s-edge2"></div>
  <div class="stack-bar">Capital Stack Hierarchy.</div>
  <div class="tier senior">
    <div class="lbl">Senior Debt</div>
    <div class="row">Revolver</div><div class="row">Asset-Based Loan</div><div class="row">Senior Term Loan</div>
    <div class="lbl">Combination</div>
    <div class="row">Unitranche</div>
  </div>
  <div class="sbox senior"><b>Senior Debt Capital Providers</b>Paid back first, plays more of a lender than partner role, less value-added, less equity dilutive, less expensive capital, but not strategically focused</div>
  <div class="dash"></div>
  <div class="tier junior">
    <div class="lbl">Junior Capital</div>
    <div class="row">Subordinated Debt</div><div class="row">Preferred Stock</div><div class="row">Common Stock</div>
  </div>
  <div class="sbox junior"><b>What Ridgefell Invests</b>Sits junior to all other capital (taking on more risk), plays a partner role, more value-added services provided, more expensive than senior debt, but supplies an engine for continuous improvement and growth</div>
  <div class="brand foot-brand"><i></i>Ridgefell</div>
  <p class="url">www.<b>ridgefellcapital</b>.com</p>
  <span class="pg">3.</span>
</section>

<!-- 5 Epilogue -->
<section class="slide c1 r3">
  <h2 class="epi">EPILOGUE</h2>
  <div class="epi-rule"></div>
  <div class="brand foot-brand"><i></i>Ridgefell</div>
  <p class="url">www.<b>ridgefellcapital</b>.com</p>
  <span class="pg">4.</span>
</section>

<!-- 6 Testimonial -->
<section class="slide c2 r3">
  <span class="qmark qm-open">“</span>
  <p class="quote">Our company had several business opportunities but I needed outside capital to take advantage of them. Why would I cede control of my business when we were at the exact point when raising outside capital would allow me to accelerate growth and achieve my life-long business and personal goals?!</p>
  <p class="cite">--Mark Ellison, CEO; The Harlan Group</p>
  <span class="qmark qm-close">”</span>
  <div class="brand foot-brand"><i></i>Ridgefell</div>
  <p class="url">www.<b>ridgefellcapital</b>.com</p>
  <span class="pg">6.</span>
</section>

<!-- 7 Uses -->
<section class="slide c1 r4">
  <h2 class="u-title">The 12 Primary Uses of Non-Control Capital</h2>
  <div class="uses">
    <div class="use"><b>Growth</b>Capital used to expand products, markets and working capital needs.</div>
    <div class="use"><b>Acquisitions</b>Capital used to buy competitors or add vertical reach.</div>
    <div class="use"><b>Partner or Shareholder Buy-Out</b>Capital used to buy out an inactive partner.</div>
    <div class="use"><b>Management Buy-Out (MBO)</b>When current management buys most or all of the owners' shares.</div>
    <div class="use"><b>Management Buy-In (MBI)</b>When outside executives buy into the business alongside current owners.</div>
    <div class="use"><b>Family Ownership &amp; Wealth Transfer</b>When ownership passes between generations of a family business.</div>
    <div class="use"><b>Balance Sheet Recapitalization</b>Changes the debt and equity mix to a better structure.</div>
    <div class="use"><b>Refinancing</b>Replacing one form of debt with better terms and flexibility.</div>
    <div class="use"><b>Family Office Support</b>Allows a family office to invest alongside junior capital.</div>
    <div class="use"><b>Senior Lender Enhancement or Transition</b>When a company needs more capital than its senior bank provides.</div>
    <div class="use"><b>De-Lever Balance Sheet</b>When a company has too much debt and needs more flexibility.</div>
    <div class="use"><b>Owner Dividend (Liquidity)</b>When owners take cash out while keeping full control.</div>
  </div>
  <div class="brand foot-brand"><i></i>Ridgefell</div>
  <p class="url">www.<b>ridgefellcapital</b>.com</p>
  <span class="pg">5.</span>
</section>

<!-- 8 Contact -->
<section class="slide c2 r4">
  <div class="banner-edge ct-edge1"></div>
  <div class="banner ct-banner">CONTACT</div>
  <div class="banner-edge ct-edge2"></div>
  <div class="ct-line"></div>
  <div class="ct ct1"><strong>Daniel R. Marlowe</strong><br>Principal &amp; Chief Marketing Officer<br>41 Alder Crest Road, Suite 210<br>Brookfield, CT 06804<br>Direct: (555) 014-2287<br>dmarlowe@<strong>ridgefellcapital</strong>.com</div>
  <div class="ct ct2"><strong>Boston Office</strong><br>18 Harbor Mill Lane, Suite 300<br>Salem, MA 01970<br><span class="bl">(555) 014-2200</span></div>
  <div class="ct ct3"><strong>San Francisco Office</strong><br>240 Market Row, Suite 410<br>San Francisco, CA 94105<br><span class="bl">(555) 019-3400</span></div>
  <div class="portrait" role="img" aria-label="Portrait photograph of the principal"></div>
  <div class="brand foot-brand"><i></i>Ridgefell</div>
  <p class="url">www.<b>ridgefellcapital</b>.com</p>
  <span class="pg">7.</span>
</section>

</body>
</html>
```